80s style fun billboard for auto repair shop

A new design for our automotive shops’s advertisement billboard with an 80s-90s theme! Neon colors like photo example. Something eye catching but easy to read. Logos attached should be altered to match theme of advertisement. 1980s or 90s colors and theme. Details need to include an arrow and “1.2 miles ahead”, phone number “903-718-2249”, address “2856 W Tallow Ave”, and “best auto repair shop in town!” . Dimensions are 12'3"x 24'6"

Target Market(s)

Drive by attention

Industry/Entity Type

Automotive

Colors

Designer to choose colors to be used in the design.

Requirements
Must have
• My logo, address, phone number, tag line and badass 90s theme look!
Nice to have
• 80s color scheme, neon colors, use example photo for color ideas

```html
<!DOCTYPE html>
<html lang="en">
<head>
<meta charset="UTF-8">
<title>RJ's Motorworks Quick Lube – Billboard</title>
<link href="https://fonts.googleapis.com/css2?family=Poppins:wght@500;600;700;800&display=swap" rel="stylesheet">
<style>
  :root {
    --page: #ffffff;
    --ink: #ffffff;
    --sky-top: #22002f;
    --sky-high: #2b0038;
    --sky-mid: #8e1a5e;
    --sky-pink: #ff3388;
    --sky-coral: #ff4a6c;
    --sky-low: #ff6a2a;
    --neon-cyan: #2ef0ff;
  }
  html, body {
    margin: 0;
    padding: 0;
    width: 1200px;
    height: 848px;
    overflow: hidden;
    background: var(--page);
    font-family: "Poppins", sans-serif;
  }
  .canvas {
    position: relative;
    width: 1200px;
    height: 848px;
  }
  .billboard {
    position: absolute;
    left: 135px;
    top: 114px;
    width: 905px;
    height: 585px;
    overflow: hidden;
    color: var(--ink);
  }
  .billboard__backdrop {
    position: absolute;
    inset: 0;
    background: linear-gradient(180deg,
      var(--sky-top) 0%,
      var(--sky-high) 16%,
      var(--sky-mid) 40%,
      var(--sky-pink) 60%,
      var(--sky-coral) 78%,
      var(--sky-low) 100%);
  }
  .tagline {
    position: absolute;
    left: 310px;
    width: 480px;
    text-align: center;
    font-weight: 800;
    margin: 0;
  }
  .tagline__best {
    top: 24px;
    font-size: 40px;
    line-height: 44px;
    letter-spacing: 4px;
  }
  .tagline__rest {
    top: 70px;
    font-size: 26px;
    line-height: 30px;
    letter-spacing: 2px;
    font-weight: 700;
  }
  .shop-name {
    position: absolute;
    left: 300px;
    top: 135px;
    width: 510px;
    height: 280px;
    display: flex;
    flex-direction: column;
    align-items: center;
    justify-content: center;
    text-align: center;
    font-weight: 800;
    color: var(--ink);
    margin: 0;
  }
  .shop-name__main {
    font-size: 120px;
    line-height: 120px;
  }
  .shop-name__sub {
    font-size: 34px;
    line-height: 40px;
  }
  .distance {
    position: absolute;
    left: 40px;
    top: 226px;
    width: 200px;
    text-align: center;
    margin: 0;
  }
  .distance__number {
    display: block;
    font-size: 122px;
    line-height: 110px;
    font-weight: 800;
    letter-spacing: -4px;
  }
  .distance__label {
    display: block;
    font-size: 25px;
    line-height: 30px;
    font-weight: 700;
    letter-spacing: 1px;
    margin-top: 2px;
  }
  .direction-arrow {
    position: absolute;
    left: 69px;
    top: 367px;
    width: 139px;
    height: 161px;
  }
  .contact {
    position: absolute;
    left: 310px;
    width: 490px;
    text-align: center;
    margin: 0;
  }
  .contact__phone {
    top: 438px;
    font-size: 58px;
    line-height: 64px;
    font-weight: 600;
    letter-spacing: 2px;
  }
  .contact__address {
    top: 500px;
    font-size: 34px;
    line-height: 40px;
    font-weight: 600;
  }
</style>
</head>
<body>
<div class="canvas">
  <section class="billboard">
    <div class="billboard__backdrop" role="img" aria-label="Neon sunset sky with palm tree silhouettes and a glowing perspective grid"></div>

    <p class="tagline tagline__best">BEST</p>
    <p class="tagline tagline__rest">AUTO REPAIR SHOP IN TOWN!</p>

    <h1 class="shop-name">
      <span class="shop-name__main">RJ'S</span>
      <span class="shop-name__sub">Motorworks Quick Lube</span>
    </h1>

    <p class="distance">
      <span class="distance__number">1.2</span>
      <span class="distance__label">MILES AHEAD</span>
    </p>

    <svg class="direction-arrow" viewBox="0 0 139 161" aria-hidden="true">
      <polygon points="69,0 139,69 103,69 103,161 36,161 36,69 0,69" fill="var(--ink)"/>
    </svg>

    <p class="contact contact__phone">903-718-2249</p>
    <p class="contact contact__address">2856 W Tallow Ave</p>
  </section>
</div>
</body>
</html>
```